The tide parlor saltwater aquarium store business card

Looking for a serious business card for a saltwater fish and coral store. I want this thing to blow people's minds when they see it. I would like the card to look very professional but I also want people to know what the tide parlor is just by seeing the card. Iam pretty open to anything as long as it's one of a kind.

Industry/Entity Type

Business

Contact Information for Business Card

18735 Calder highway Harrow Falls pa 16172. Thetideparlor.com. Customerservice@thetideparlor.com. 5038826417

Requirements
Should not have
• Please no child like fish designs

```html
<!DOCTYPE html>
<html lang="en">
<head>
<meta charset="utf-8">
<title>The Tide Parlor — Business Card</title>
<link rel="stylesheet" href="https://fonts.googleapis.com/css2?family=Open+Sans:wght@400;600&display=swap">
<style>
  :root {
    --stage: #e9ebee;
    --card-blue: #3f6189;
    --card-white: #ffffff;
    --ink: #2b2b2b;
    --accent-blue: #4a86c5;
    --icon-blue: #3f6189;
    --rule: #d9d9d9;
    --shadow: rgba(20, 30, 45, 0.18);
  }
  * { box-sizing: border-box; margin: 0; padding: 0; }
  html, body {
    width: 1200px; height: 864px; overflow: hidden;
    background: var(--stage);
    font-family: "Open Sans", Arial, sans-serif;
  }
  .canvas { position: relative; width: 1200px; height: 864px; }

  .card {
    position: absolute;
    width: 560px; height: 320px;
    box-shadow: 0 8px 24px var(--shadow);
  }
  .card--front { left: 180px; top: 70px; background: var(--card-blue); }
  .card--back  { left: 460px; top: 470px; background: var(--card-white); }

  .brand {
    position: absolute;
    display: flex; align-items: center; gap: 14px;
    font-weight: 600;
    white-space: nowrap;
  }
  .brand__dot {
    width: 40px; height: 40px; border-radius: 50%;
  }
  .card--front .brand {
    left: 50%; top: 50%; transform: translate(-50%, -50%);
    color: var(--card-white); font-size: 38px;
  }
  .card--front .brand__dot { border: 3px solid var(--card-white); }

  .card--back .brand {
    right: 44px; top: 52px;
    color: var(--ink); font-size: 30px;
  }
  .card--back .brand__dot { width: 34px; height: 34px; background: var(--accent-blue); }

  .address {
    position: absolute; left: 40px; top: 120px;
    font-size: 15px; line-height: 26px; color: var(--ink);
  }
  .rule {
    position: absolute; left: 150px; right: 40px; top: 184px;
    height: 1px; background: var(--rule);
  }
  .contacts {
    position: absolute; right: 34px; bottom: 36px;
    list-style: none; text-align: right;
    font-size: 15px; line-height: 24px; color: var(--ink);
  }
  .contacts li { display: flex; justify-content: flex-end; align-items: center; gap: 10px; }
  .contacts svg { width: 16px; height: 16px; flex: none; }
</style>
</head>
<body>
<main class="canvas">
  <section class="card card--front" aria-label="Business card front">
    <div class="brand"><span class="brand__dot"></span><span class="brand__name">The Tide Parlor</span></div>
  </section>

  <section class="card card--back" aria-label="Business card back">
    <div class="brand"><span class="brand__dot"></span><span class="brand__name">The Tide Parlor</span></div>
    <p class="address">18735 Calder highway<br>Harrow Falls pa 16172.</p>
    <div class="rule"></div>
    <ul class="contacts">
      <li>5038826417
        <svg viewBox="0 0 16 16" aria-hidden="true"><rect width="16" height="16" rx="2" fill="var(--icon-blue)"/><path d="M4 6c0-1 1-2 4-2s4 1 4 2l-1 1-2-1V5H7v1L5 7zM5 8h6l1 4H4z" fill="#fff"/></svg>
      </li>
      <li>Customerservice@thetideparlor.com
        <svg viewBox="0 0 16 16" aria-hidden="true"><rect width="16" height="16" rx="2" fill="var(--icon-blue)"/><rect x="3.5" y="5" width="9" height="6.5" fill="none" stroke="#fff" stroke-width="1.2"/><path d="M3.5 5 8 8.6 12.5 5" fill="none" stroke="#fff" stroke-width="1.2"/></svg>
      </li>
      <li>www.thetideparlor.com
        <svg viewBox="0 0 16 16" aria-hidden="true"><rect width="16" height="16" rx="2" fill="var(--icon-blue)"/><path d="M7 9.5 5.5 11a1.8 1.8 0 0 1-2.5-2.5L4.5 7M9 6.5 10.5 5A1.8 1.8 0 0 1 13 7.5L11.5 9M6.5 9.5l3-3" fill="none" stroke="#fff" stroke-width="1.3" stroke-linecap="round"/></svg>
      </li>
    </ul>
  </section>
</main>
</body>
</html>
```